Harlow Ridge Growers and Nursery needs a business street sign.

I have three businesses located at the same address: The Harlow Ridge Growers & Nursery, The Bramble Nook, and The Quarry Commons. I am looking for a 4’ x 8’ street sign to represent all three businesses as one retail experience. It needs to be eye catching yet simple enough that people can fully read it while driving by. I have logos for the greenhouse and village however I do not have anything for The Bramble Nook. I’m looking for some type of font that’s similar or in between the two attached logos for The Bramble Nook.

• Horizontal Sign, Eye catching, yet simple design so people see it while driving by.
• Horizontal Sign
• I’m open to the design being both vertical and horizontal. Please provide both options

```html
<!DOCTYPE html>
<html lang="en">
<head>
<meta charset="utf-8">
<title>Harlow Ridge Growers &amp; Nursery – Street Sign</title>
<link rel="stylesheet" href="https://fonts.googleapis.com/css2?family=Poppins:wght@700&display=swap">
<style>
  :root {
    --backdrop: #e4e4e4;
    --sign-face: #ffffff;
    --brand-green: #076a45;
    --brand-brick: #9a3328;
    --divider-tan: #c48a6a;
    --text-light: #ffffff;
  }
  * { margin: 0; padding: 0; box-sizing: border-box; }
  html, body {
    width: 1200px;
    height: 1200px;
    overflow: hidden;
    background: var(--backdrop);
    font-family: "Poppins", sans-serif;
  }
  .street-sign {
    position: absolute;
    left: 40px;
    top: 320px;
    width: 1120px;
    height: 560px;
    background: var(--sign-face);
  }
  .visit-tab {
    position: absolute;
    left: 0;
    top: 0;
    width: 514px;
    height: 237px;
  }
  .visit-tab__label {
    position: absolute;
    left: 50px;
    top: 52px;
    font-size: 52px;
    line-height: 1;
    color: var(--text-light);
    letter-spacing: 0.5px;
  }
  .business-name {
    position: absolute;
    font-weight: 700;
    text-align: center;
    line-height: 1.08;
  }
  .business-name--growers {
    left: 560px;
    top: 58px;
    width: 520px;
    font-size: 46px;
    color: var(--brand-green);
  }
  .business-name--commons {
    left: 30px;
    top: 360px;
    width: 510px;
    font-size: 60px;
    color: var(--brand-brick);
  }
  .business-name--bramble {
    left: 580px;
    top: 360px;
    width: 520px;
    font-size: 60px;
    color: var(--brand-green);
  }
  .sign-divider {
    position: absolute;
    left: 559px;
    top: 320px;
    width: 2px;
    height: 212px;
    background: var(--divider-tan);
  }
</style>
</head>
<body>
  <main class="street-sign">
    <div class="visit-tab">
      <svg width="514" height="237" viewBox="0 0 514 237" aria-hidden="true">
        <path d="M0 0 H514 L400 146 C350 208 290 237 211 237 H0 Z" fill="var(--brand-green)"/>
        <g fill="var(--text-light)">
          <rect x="62" y="167" width="188" height="9"/>
          <path d="M50 171.5 L78 147 H97 L72 171.5 L97 196 H78 Z"/>
        </g>
      </svg>
      <p class="visit-tab__label">VISIT OUR...</p>
    </div>

    <h1 class="business-name business-name--growers">The Harlow Ridge<br>Growers &amp; Nursery</h1>

    <h2 class="business-name business-name--commons">Quarry<br>Commons</h2>

    <div class="sign-divider"></div>

    <h2 class="business-name business-name--bramble">The Bramble<br>Nook</h2>
  </main>
</body>
</html>
```